Professional & attention grabbing.

A business card design, front and back. I already have a logo I will attach, but I am open to something new as well.
Things to include:
Name:
Title:
Phone:
Email:
Wanting something that is professional but attention grabbing.
Also we do a lot of work using drones on natural gas pipelines (leading the future)if you want to include any of that. I'm open to ideas.
Target Market(s)
Natural gas transmission industry / greenhouse gas mitigation industry
Industry/Entity Type
Business
Contact Information for Business Card
All details have been conveyed above.
Colors
Designer to choose colors to be used in the design.
Look and feel
Each slider illustrates characteristics of the customer's brand and the style your logo design should communicate.

```html
<!DOCTYPE html>
<html lang="en">
<head>
<meta charset="utf-8">
<title>Tarnwell Inspections – Business Card</title>
<link href="https://fonts.googleapis.com/css2?family=Open+Sans:wght@400;600;700&display=swap" rel="stylesheet">
<style>
  :root {
    --brand-red: #c0222a;
    --brand-black: #1c1c1c;
    --ink-dark: #1e1616;
    --paper-white: #ffffff;
    --backdrop: #e4e2df;
  }
  * { margin: 0; padding: 0; box-sizing: border-box; }
  html, body {
    width: 1200px; height: 1000px; overflow: hidden;
    background: var(--backdrop);
    font-family: "Open Sans", Arial, sans-serif;
  }
  .stage { position: relative; width: 1200px; height: 1000px; }

  .card {
    position: absolute; left: 266px; width: 666px; height: 396px; overflow: hidden;
  }
  .card-front { top: 75px; background: var(--brand-red); }
  .card-back { top: 534px; background: var(--brand-black); }

  .side-band {
    position: absolute; top: 0; right: 0; width: 232px; height: 100%;
    background: var(--brand-black);
  }

  .wordmark { position: absolute; display: flex; align-items: center; font-weight: 700; }
  .wordmark-square { flex: none; }
  .wordmark-name { line-height: 1.05; text-transform: uppercase; letter-spacing: 0.5px; }

  .card-front .wordmark { left: 32px; top: 30px; color: var(--ink-dark); }
  .card-front .wordmark-square { width: 58px; height: 58px; background: var(--ink-dark); margin-right: 16px; }
  .card-front .wordmark-name { font-size: 27px; }

  .card-back .wordmark { left: 129px; top: 123px; color: var(--paper-white); }
  .card-back .wordmark-square { width: 148px; height: 150px; background: var(--brand-red); margin-right: 32px; }
  .card-back .wordmark-name { font-size: 42px; }

  .contact { position: absolute; left: 33px; top: 185px; color: var(--ink-dark); }
  .contact-name { font-size: 19px; font-weight: 600; color: var(--paper-white); letter-spacing: 0.3px; line-height: 24px; }
  .contact-title { font-size: 15px; line-height: 20px; }
  .contact-address { margin-top: 20px; font-size: 15px; line-height: 20px; }
  .contact-lines { margin-top: 12px; list-style: none; font-size: 15px; line-height: 24px; }
  .contact-lines li { display: flex; align-items: center; }
  .contact-lines svg { width: 12px; height: 12px; margin-right: 10px; fill: var(--ink-dark); }
</style>
</head>
<body>
<main class="stage">
  <section class="card card-front" aria-label="Card front">
    <div class="wordmark">
      <span class="wordmark-square"></span>
      <span class="wordmark-name">Tarnwell<br>Inspections</span>
    </div>
    <div class="contact">
      <p class="contact-name">DAREN HOLTBY</p>
      <p class="contact-title">Managing Director</p>
      <p class="contact-address">2148 North Calder Road<br>Linwood, MD 21790</p>
      <ul class="contact-lines">
        <li><svg viewBox="0 0 12 12"><path d="M1 4c0-2 2-3 5-3s5 1 5 3v1H8V4H4v1H1zM2 6h8l1 5H1z"/></svg>+ 000 000 0000</li>
        <li><svg viewBox="0 0 12 12"><path d="M0 2h12v1L6 7 0 3zM0 4.5l6 4 6-4V10H0z"/></svg>info@tarnwell.com</li>
        <li><svg viewBox="0 0 12 12"><circle cx="6" cy="6" r="5.5"/></svg>www.tarnwell.com</li>
      </ul>
    </div>
    <div class="side-band"></div>
  </section>

  <section class="card card-back" aria-label="Card back">
    <div class="wordmark">
      <span class="wordmark-square"></span>
      <span class="wordmark-name">Tarnwell<br>Inspections</span>
    </div>
  </section>
</main>
</body>
</html>
```